Zentrova - Creative Automation

We are a software house for Audio Visual Systems integration/automation and home automation. we develop innovative software to automate a variety of devices mainly related to audio visuals and we design touch panel user interfaces to control these systems.

We would like to see designs that stick to our colours and theme, which you can find on our webpage www.zentrova.com.au

The final design should communicate touch panels, innovation, software and automation.

Industry/Entity Type

Software

Requirements
Must have
• The business card must show the following information:
Name example : Derek Malloway
Qualification example: B Eng ICT(CompSys) Dip EngPrac
Title example : Control Systems Programmer
Mobile Phone, Company phone, Email address ,Company website

```html
<!DOCTYPE html>
<html lang="en">
<head>
<meta charset="utf-8">
<title>Zentrova – Business Card</title>
<link rel="stylesheet" href="https://fonts.googleapis.com/css2?family=Lato:wght@400;700;900&display=swap">
<style>
  :root {
    --brand-blue: #0f78c0;
    --brand-green: #1f9a4a;
    --ink: #333333;
    --card-white: #ffffff;
    --backdrop-light: #f2f2f2;
    --backdrop-dark: #a9a9a9;
    --photo-dark: #2b2f33;
    --photo-mid: #8a9096;
  }
  * { box-sizing: border-box; margin: 0; padding: 0; }
  html, body { width: 1200px; height: 900px; overflow: hidden; }
  body {
    background: radial-gradient(ellipse at 50% 45%, var(--backdrop-light) 0%, #d9d9d9 55%, var(--backdrop-dark) 100%);
    font-family: "Lato", sans-serif;
    position: relative;
  }
  .card {
    position: absolute;
    width: 560px;
    height: 320px;
    border-radius: 18px;
    overflow: hidden;
    box-shadow: 0 10px 28px rgba(0,0,0,0.28);
  }
  .card--front { left: 320px; top: 90px; background: var(--brand-blue); }
  .card--back  { left: 320px; top: 470px; background: var(--card-white); }

  /* Front */
  .front-brand {
    position: absolute; inset: 0;
    display: flex; flex-direction: column; align-items: center; justify-content: center;
    color: var(--card-white);
  }
  .front-brand__square {
    width: 110px; height: 84px; border-radius: 14px;
    background: var(--card-white); margin-bottom: 22px;
  }
  .front-brand__name {
    font-weight: 900; font-size: 72px; letter-spacing: 1px; line-height: 1;
  }
  .front-brand__tagline {
    font-weight: 900; font-size: 15px; margin-top: 6px;
  }

  /* Back */
  .back-photo {
    position: absolute; left: 0; top: 0; width: 330px; height: 100%;
    background: linear-gradient(100deg, var(--photo-dark) 0%, #4a5056 35%, var(--photo-mid) 60%, rgba(255,255,255,0) 100%);
  }
  .back-brand {
    position: absolute; left: 150px; top: 24px;
    display: flex; align-items: center; gap: 12px;
  }
  .back-brand__square {
    width: 82px; height: 62px; border-radius: 10px; background: var(--brand-blue);
  }
  .back-brand__text { display: flex; flex-direction: column; align-items: flex-end; }
  .back-brand__name {
    font-weight: 900; font-size: 46px; line-height: 1; color: var(--brand-green);
  }
  .back-brand__tagline {
    font-weight: 900; font-size: 11px; color: var(--brand-blue); margin-top: 2px;
  }
  .person {
    position: absolute; left: 320px; top: 116px;
  }
  .person__name {
    font-weight: 700; font-size: 18px; letter-spacing: 1px; color: var(--brand-green);
    text-transform: uppercase; margin-left: 12px; margin-bottom: 2px;
  }
  .person__line { font-size: 12.5px; color: var(--ink); line-height: 1.35; }
  .contacts {
    position: absolute; left: 312px; top: 200px;
    list-style: none; font-size: 13px; color: var(--ink); line-height: 1.3;
  }
  .contacts li { display: flex; gap: 10px; }
  .contacts__label {
    width: 18px; font-weight: 700; font-style: italic; color: var(--brand-green);
  }
</style>
</head>
<body>
  <section class="card card--front" aria-label="Business card front">
    <div class="front-brand">
      <div class="front-brand__square"></div>
      <div class="front-brand__name">zentrova</div>
      <div class="front-brand__tagline">Creative Automation</div>
    </div>
  </section>

  <section class="card card--back" aria-label="Business card back">
    <div class="back-photo" role="img" aria-label="Photo of a businessman in a dark suit touching floating touch-panel screens"></div>
    <div class="back-brand">
      <div class="back-brand__square"></div>
      <div class="back-brand__text">
        <div class="back-brand__name">zentrova</div>
        <div class="back-brand__tagline">Creative Automation</div>
      </div>
    </div>
    <div class="person">
      <div class="person__name">Derek Malloway</div>
      <div class="person__line">B Eng ICT(CompSys) Dip EngPrac</div>
      <div class="person__line">Control Systems Programmer</div>
    </div>
    <ul class="contacts">
      <li><span class="contacts__label">T:</span><span>0142 318 607</span></li>
      <li><span class="contacts__label">F:</span><span>0198 275 430</span></li>
      <li><span class="contacts__label">E:</span><span>derekmalloway@zentrova.com</span></li>
      <li><span class="contacts__label">W:</span><span>www.zentrova.com</span></li>
    </ul>
  </section>
</body>
</html>
```